New Public Cloud Consulting Needs Powerpoint Template

Setting up a new consulting practice and need a powerpoint template and design that reflects our vision. We focus on KLV Public Cloud only. We want to emphasize innovation, cloud, speed. We are based in Asia, with headquarters in Singapore. We serve Asia and Europe customers. The attached file is the current template and logo that we use. However it is not dynamic enough. Blue is the color of our logo - but we must have other colors that complement the blue.

Target Market(s)

Innovation, cloud, advisory

Font styles to use
Other font styles liked:
• We want a different font that what is included in the file.

Requirements
Must have
• Logo which is included in the sample template and blue color - however we want other colors included. To date - most of the designs are completely blue - which we do not want. Additionally we need to create an image of innovation, future vision. Please do not include a picture of a cloud. That is not innovative.
Nice to have
• Would be nice to show people in some of the slides - professional etc. There is one slide in the attached presentation that gives you an idea of this concept. How else can we do this ?

```html
<!DOCTYPE html>
<html lang="en">
<head>
<meta charset="utf-8">
<title>NOVA Advisory Group – KLV Public Cloud Presentation Template</title>
<link href="https://fonts.googleapis.com/css2?family=Work+Sans:ital,wght@0,400;0,500;0,600;0,700;1,400&display=swap" rel="stylesheet">
<style>
:root{
  --navy:#1f3870;
  --ink:#1c2540;
  --blue:#3566d6;
  --sky:#7ea6e6;
  --pale:#a9c2ef;
  --teal:#14a89a;
  --mint:#6fd3c6;
  --amber:#f29a3d;
  --grey:#8b93a3;
}
*{box-sizing:border-box;margin:0;padding:0}
html,body{width:1200px;height:1175px;overflow:hidden}
body{background:linear-gradient(160deg,#a9acb0,#9b9ea3);font-family:"Work Sans",sans-serif;color:var(--ink);position:relative}
.slide{position:absolute;width:363px;height:204px;background:#fff;box-shadow:2px 3px 7px rgba(0,0,0,.28);overflow:hidden}
.abs{position:absolute}
.heading{position:absolute;left:13px;top:12px;font-size:12.5px;color:var(--navy);font-weight:400;white-space:nowrap}
.heading b{font-weight:700}
.heading::after{content:"";position:absolute;left:0;top:19px;width:18px;height:2px;background:var(--teal);border-radius:1px}
.brand{position:absolute;right:11px;top:11px;display:flex;align-items:center;gap:2px;font-size:8px;font-weight:700;color:var(--navy)}
.brand i{display:block;width:5px;height:5px;background:var(--teal)}
.foot{position:absolute;left:13px;right:13px;bottom:11px;border-bottom:.7px solid var(--sky);font-size:2.6px;color:var(--grey);display:flex;justify-content:space-between;padding-bottom:1px}
.foot span:last-child{font-size:3.5px;color:var(--ink)}
.t{font-size:3px;line-height:1.35;color:var(--grey)}
.tt{font-size:4px;line-height:1.35;color:var(--grey)}
.photo{position:absolute;background:linear-gradient(135deg,#c9ced6,#8c96a8 60%,#5d6a80)}
.num{color:var(--teal);font-weight:700}
.sub{font-size:5.5px;font-weight:600;color:var(--navy)}
.toc-row{position:relative;height:21px;border-bottom:.6px solid #c3c8d2;width:124px}
.toc-row span{position:absolute;left:127px;top:2px;width:8px;height:8px;border-radius:50%;background:var(--teal);color:#fff;font-size:3.5px;text-align:center;line-height:8px}
.tile{position:absolute;width:57px;height:55px;padding:6px 7px;color:#fff}
.tile b{display:block;font-size:5px;font-weight:700;margin-top:16px}
.tile p{font-size:2.6px;line-height:1.3}
.step{flex:none;width:11px;height:11px;color:#fff;font-size:7px;font-weight:700;text-align:center;line-height:11px}
.phone{position:absolute;width:43px;height:89px;border:1.6px solid #222;border-radius:5px;background:#fff}
.phone i{position:absolute;left:15px;top:1px;width:10px;height:2px;border-radius:1px;background:#222}
</style>
</head>
<body>

<!-- 1 Title -->
<section class="slide" style="left:39px;top:38px">
  <div class="photo" role="img" aria-label="Grey-toned office building with a businesswoman on the phone" style="left:120px;top:0;width:243px;height:204px;background:linear-gradient(90deg,#fff 0%,#e6e8ec 25%,#b9bec6 70%,#a4aab4)"></div>
  <svg class="abs" style="left:0;top:0" width="363" height="204"><polygon points="148,204 260,12 363,204" fill="#3a6fdc" opacity=".72"/><polygon points="300,204 335,140 363,192 363,204" fill="#14a89a" opacity=".8"/></svg>
  <i class="abs" style="left:7px;top:6px;width:6px;height:6px;background:var(--amber)"></i>
  <div class="abs" style="left:26px;top:30px;display:flex;align-items:center;gap:4px;font-size:14px;font-weight:700;color:var(--navy)"><i style="display:block;width:9px;height:9px;background:var(--teal)"></i>NOVA Advisory Group</div>
  <div class="abs" style="left:19px;top:88px;font-size:17px;font-weight:700;color:var(--navy)">Presentation Title</div>
  <div class="abs" style="left:19px;top:108px;font-size:17px;color:var(--blue)">Goes Here</div>
  <div class="abs" style="left:19px;top:134px;font-size:8.5px;font-weight:600;color:var(--teal)">Presentation Template</div>
  <div class="abs" style="left:19px;top:146px;font-size:4.8px;color:#444;width:150px;line-height:1.3">Lorem Ipsum is simply dummy text of the printing and typesetting industry.</div>
  <div class="abs" style="left:19px;top:184px;font-size:4px;letter-spacing:.6px;color:#444">Friday, Feb 18, 2026</div>
</section>

<!-- 2 Business Marketing -->
<section class="slide" style="left:420px;top:38px">
  <svg class="abs" style="left:0;top:0" width="363" height="204">
    <polygon points="162,0 363,0 363,90 264,48 122,204 108,204" fill="#3a6fdc"/>
    <polygon points="230,0 363,0 363,40 300,0" fill="#6fd3c6"/>
    <polygon points="178,0 240,0 128,170" fill="#7ea6e6" opacity=".8"/>
    <polygon points="264,48 118,204 363,204 363,120" fill="#fff"/>
  </svg>
  <div class="photo" role="img" aria-label="Team of professionals gathered around a laptop" style="left:0;top:0;width:363px;height:204px;clip-path:polygon(264px 58px,130px 204px,363px 204px,363px 132px);background:linear-gradient(160deg,#d8dde5,#8e97a8 55%,#4f5b70)"></div>
  <i class="abs" style="left:17px;top:24px;width:1px;height:52px;background:var(--navy)"></i>
  <div class="abs" style="left:21px;top:27px;font-size:18.5px;font-weight:700;color:var(--navy);line-height:1.05">Business<br>Marketing</div>
  <div class="abs" style="left:17px;top:90px;font-size:11px;color:var(--teal);line-height:1.2">Presentation<br>Template</div>
  <div class="abs" style="left:17px;top:124px;font-size:4.5px;color:#444;width:80px;line-height:1.3">Lorem Ipsum is simply dummy text of the printing and typesetting industry.</div>
  <div class="abs" style="left:17px;top:164px;display:flex;align-items:center;gap:3px;font-size:7.5px;font-weight:700;color:var(--navy)"><i style="display:block;width:6px;height:6px;background:var(--teal)"></i>NOVA Advisory Group</div>
</section>

<!-- 3 Table of Contents -->
<section class="slide" style="left:798px;top:38px">
  <div class="heading">Table of <b>Contents</b></div>
  <div class="brand"><i></i>NOVA</div>
  <div class="photo" role="img" aria-label="Two business people shaking hands" style="left:38px;top:55px;width:122px;height:108px"></div>
  <div class="abs" style="left:181px;top:62px;width:140px;font-size:5px;color:var(--navy)">
    <div class="toc-row">• Simple Text One<span>02</span></div>
    <div class="toc-row">• Simple Text Two<span style="background:var(--blue)">04</span></div>
    <div class="toc-row">• Simple Text Three<span style="background:var(--amber)">06</span></div>
    <div class="toc-row">• Simple Text Four<span>08</span></div>
    <div class="toc-row">• Simple Text Five<span style="background:var(--blue)">10</span></div>
  </div>
  <div class="foot"><span>© 2025 NOVA Advisory Group. All rights reserved.</span><span>2</span></div>
</section>

<!-- 4 Mission / Vision -->
<section class="slide" style="left:39px;top:259px">
  <div class="heading" style="left:19px"><b>Heading</b> Goes Here</div>
  <div class="brand"><i></i>NOVA</div>
  <div class="abs" style="left:22px;top:39px;width:150px;font-size:5.5px;font-style:italic;color:#555;line-height:1.3">Lorem ipsum dolor sit amet, cons ectetuer adipiscing elit, sed diam nonummy nibh euis­mod tincidunt.Lorem ipsum dolor sit amet.</div>
  <div class="photo" role="img" aria-label="Presenter at a whiteboard with a seated audience" style="left:25px;top:81px;width:149px;height:87px;border-radius:8px"></div>
  <div class="abs" style="left:199px;top:69px;width:31px;height:35px;border-radius:3px;background:var(--blue)"><svg width="31" height="35"><path d="M9 20 L19 12 L21 24 Z M11 21 L13 27" stroke="#fff" stroke-width="1.4" fill="none"/><path d="M23 12 l3-2 M24 16 h3" stroke="#fff" stroke-width="1"/></svg></div>
  <div class="abs" style="left:199px;top:126px;width:31px;height:35px;border-radius:3px;background:var(--teal)"><svg width="31" height="35"><path d="M9 24 L22 11 M9 11 L22 24" stroke="#fff" stroke-width="1.5"/></svg></div>
  <div class="abs" style="left:237px;top:69px;font-size:8px;color:var(--blue);font-weight:600">Our <span style="color:var(--navy)">Mission</span></div>
  <div class="abs t" style="left:237px;top:80px;width:105px;font-size:4.3px;font-style:italic">Lorem ipsum dolor sit amet, cons ectetuer adipiscing elit, sed diam nonummy nibh euismod tincidunt.</div>
  <div class="abs" style="left:237px;top:127px;font-size:8px;color:var(--teal);font-weight:600">Our <span style="color:var(--navy)">Vision</span></div>
  <div class="abs t" style="left:237px;top:138px;width:105px;font-size:4.3px;font-style:italic">Lorem ipsum dolor sit amet, cons ectetuer adipiscing elit, sed diam nonummy nibh euismod tincidunt.</div>
  <div class="foot"><span>© 2025 NOVA Advisory Group. All rights reserved.</span><span>2</span></div>
</section>

<!-- 5 Idea Promotion Growth -->
<section class="slide" style="left:420px;top:259px">
  <div class="heading"><b>Heading</b> Goes Here</div>
  <div class="brand"><i></i>NOVA</div>
  <div class="abs" role="img" aria-label="Faint world map" style="left:50px;top:38px;width:265px;height:130px;border-radius:50%;background:radial-gradient(ellipse,#eef0f3 40%,rgba(255,255,255,0) 72%)"></div>
  <svg class="abs" style="left:0;top:0" width="363" height="204" fill="none" stroke="#1f3870" stroke-width="1.6">
    <rect x="68" y="52" width="61" height="93" rx="5"/>
    <rect x="151" y="52" width="61" height="93" rx="5"/>
    <rect x="234" y="52" width="61" height="93" rx="5"/>
    <path d="M129 110 L151 72" stroke="#fff" stroke-width="5"/>
    <path d="M212 110 L234 72" stroke="#fff" stroke-width="5"/>
    <path d="M124 110 L156 72 M207 110 L239 72"/>
    <circle cx="123" cy="79" r="2.2" fill="#14a89a" stroke="#14a89a"/><circle cx="157" cy="118" r="2.2" fill="#14a89a" stroke="#14a89a"/>
    <circle cx="207" cy="79" r="2.2" fill="#f29a3d" stroke="#f29a3d"/><circle cx="240" cy="118" r="2.2" fill="#f29a3d" stroke="#f29a3d"/>
    <g stroke-width=".8"><circle cx="98.5" cy="72" r="3" stroke="#14a89a"/><path d="M97 76 h3" stroke="#14a89a"/><g stroke="#3566d6"><rect x="178" y="71" width="8" height="6"/><path d="M178 71 l4 3 l4-3"/></g><path d="M259 70 v8 h9 M261 76 l3-3 l2 2 l3-4" stroke="#f29a3d"/></g>
  </svg>
  <div class="abs" style="left:68px;top:82px;width:61px;text-align:center;font-size:5px;font-weight:600;color:var(--teal)">IDEA</div>
  <div class="abs" style="left:151px;top:82px;width:61px;text-align:center;font-size:5px;font-weight:600;color:var(--blue)">PROMOTION</div>
  <div class="abs" style="left:234px;top:82px;width:61px;text-align:center;font-size:5px;font-weight:600;color:var(--amber)">GROWTH</div>
  <div class="abs t" style="left:73px;top:91px;width:51px;text-align:center;font-size:2.7px">Lorem ipsum dolor sit amet, consectetuer adipiscing elit, sed diam nonummy nibh euismod tincidunt ut laoreet dolore magna aliquam erat volutpat. Ut wisi enim ad minim veniam.</div>
  <div class="abs t" style="left:156px;top:91px;width:51px;text-align:center;font-size:2.7px">Lorem ipsum dolor sit amet, consectetuer adipiscing elit, sed diam nonummy nibh euismod tincidunt ut laoreet dolore magna aliquam erat volutpat. Ut wisi enim ad minim veniam.</div>
  <div class="abs t" style="left:239px;top:91px;width:51px;text-align:center;font-size:2.7px">Lorem ipsum dolor sit amet, consectetuer adipiscing elit, sed diam nonummy nibh euismod tincidunt ut laoreet dolore magna aliquam erat volutpat. Ut wisi enim ad minim veniam.</div>
  <div class="abs" style="left:45px;top:157px;width:273px;text-align:center;font-size:4px;color:#555;line-height:1.3">Lorem ipsum dolor sit amet, consectetuer adipiscing elit, sed diam nonummy nibh euismod tincidunt ut laoreet dolore magna aliquam erat volutpat. Ut wisi enim ad minim veniam, quis nostrud exerci tation ullamcorper suscipit lobortis nisl ut aliquip ex ea commodo consequat. Duis autem vel eum iriure dolor in hendrerit</div>
  <div class="foot"><span>© 2025 NOVA Advisory Group. All rights reserved.</span><span>3</span></div>
</section>

<!-- 6 List + navy panel -->
<section class="slide" style="left:798px;top:259px">
  <div class="heading"><b>Heading</b> Goes Here</div>
  <div class="brand"><i></i>NOVA</div>
  <div class="abs" style="left:38px;top:50px;width:130px">
    <div class="sub"><span class="num">01.</span> Aliquam Erat Volutpat</div><div class="t" style="margin-left:10px;width:120px">Lorem ipsum dolor sit amet, consectetuer adipiscing elit, sed diam nonummy nibh euismod</div>
    <div class="sub" style="margin-top:16px"><span class="num">02.</span> Consectetuer Adipiscing Elit</div><div class="t" style="margin-left:10px;width:120px">Lorem ipsum dolor sit amet, consectetuer adipiscing elit, sed diam nonummy nibh euismod tincidunt ut laoreet</div>
    <div class="sub" style="margin-top:16px"><span class="num">03.</span> Duis Autem Vel Eum</div><div class="t" style="margin-left:10px;width:120px">Lorem ipsum dolor sit amet, consectetuer adipiscing elit, sed diam nonummy nibh euismod tincidunt.</div>
    <div class="sub" style="margin-top:16px"><span class="num">04.</span> Aliquam Erat Volutpat</div><div class="t" style="margin-left:10px;width:120px">Lorem ipsum dolor sit amet, consectetuer adipiscing elit, sed diam nonummy nibh euismod tincidunt ut laoreet.</div>
  </div>
  <div class="abs" style="left:195px;top:46px;width:124px;height:126px;border-radius:9px;background:var(--navy)"></div>
  <div class="abs" style="left:183px;top:58px;width:26px;height:26px;border-radius:50%;background:var(--teal);border:2px solid #fff"></div>
  <div class="abs" style="left:183px;top:95px;width:26px;height:26px;border-radius:50%;background:var(--blue);border:2px solid #fff"></div>
  <div class="abs" style="left:183px;top:134px;width:26px;height:26px;border-radius:50%;background:var(--amber);border:2px solid #fff"></div>
  <svg class="abs" style="left:183px;top:58px" width="26" height="102" fill="none" stroke="#fff" stroke-width="1"><rect x="8" y="9" width="10" height="7"/><path d="M11 19h4"/><path d="M8 52 a4 4 0 0 1 4-5 a4 4 0 0 1 7 2 a3 3 0 0 1 0 5 h-11 z M13 54v5"/><path d="M7 94 l4-4 l4 3 l5-5"/><circle cx="7" cy="94" r="1.3"/><circle cx="11" cy="90" r="1.3"/><circle cx="15" cy="93" r="1.3"/><circle cx="20" cy="88" r="1.3"/></svg>
  <div class="abs" style="left:217px;top:60px;width:95px;color:#fff"><div style="font-size:6.3px;font-weight:600;color:var(--mint)">LOREM IPSUM</div><div style="font-size:3px;line-height:1.25">ipsum dolor sit amet, cons ectetuer adipiscing elit, sed diam nonummy nibh euismod tincidunt ut laoreet</div></div>
  <div class="abs" style="left:217px;top:97px;width:95px;color:#fff"><div style="font-size:6.3px;font-weight:600;color:var(--pale)">LOREM IPSUM</div><div style="font-size:3px;line-height:1.25">ipsum dolor sit amet, cons ectetuer adipiscing elit, sed diam nonummy nibh euismod tincidunt ut laoreet dolore magna aliquam erat volutpat.</div></div>
  <div class="abs" style="left:217px;top:137px;width:95px;color:#fff"><div style="font-size:6.3px;font-weight:600;color:#f8c58c">LOREM IPSUM</div><div style="font-size:3px;line-height:1.25">ipsum dolor sit amet, cons ectetuer adipiscing elit, sed diam nonummy nibh euismod tincidunt</div></div>
  <div class="foot"><span>© 2025 NOVA Advisory Group. All rights reserved.</span><span>4</span></div>
</section>

<!-- 7 Problem / Solution tiles -->
<section class="slide" style="left:39px;top:481px">
  <div class="heading"><b>Heading</b> Goes Here</div>
  <div class="brand"><i></i>NOVA</div>
  <div class="abs" style="left:26px;top:68px;width:80px"><div class="sub"><span class="num">01.</span> Project Problem</div><div class="t" style="width:80px">Lorem ipsum dolor sit amet, cons ectetuer adipiscing elit, sed diam nonummy nibh euismod tincidunt.Lorem ipsum dolor sit amet.</div></div>
  <div class="abs" style="left:120px;top:68px;width:80px"><div class="sub"><span class="num">02.</span> Project Solution</div><div class="t" style="width:80px">Lorem ipsum dolor sit amet, cons ectetuer adipiscing elit, sed diam nonummy nibh euismod tincidunt.Lorem ipsum dolor sit amet.</div></div>
  <div class="abs" style="left:26px;top:117px;width:80px"><div class="sub"><span class="num">03.</span> Project Problem</div><div class="t" style="width:80px">Lorem ipsum dolor sit amet, cons ectetuer adipiscing elit, sed diam nonummy nibh euismod tincidunt.Lorem ipsum dolor sit amet.</div></div>
  <div class="abs" style="left:120px;top:117px;width:80px"><div class="sub"><span class="num">04.</span> Project Solution</div><div class="t" style="width:80px">Lorem ipsum dolor sit amet, cons ectetuer adipiscing elit, sed diam nonummy nibh euismod tincidunt.Lorem ipsum dolor sit amet.</div></div>
  <div class="tile" style="left:214px;top:51px;background:var(--teal);border-top-left-radius:6px"><div style="width:7px;height:7px;border:1px solid #fff;border-radius:50%"></div><b>PROBLEM</b><p>Lorem ipsum dolor sit amet, cons ectetuer adipiscing elit, sed diam nonummy.</p></div>
  <div class="tile" style="left:275px;top:51px;background:var(--navy);border-top-right-radius:6px"><div style="width:7px;height:7px;border:1px solid #fff;border-radius:50%"></div><b>SOLUTION</b><p>Lorem ipsum dolor sit amet, cons ectetuer adipiscing elit, sed diam nonummy.</p></div>
  <div class="tile" style="left:214px;top:110px;background:var(--blue);border-bottom-left-radius:6px"><svg width="9" height="8" fill="none" stroke="#fff" stroke-width=".8"><path d="M1 7h8M2 7V4M4.5 7V2M7 7V3"/></svg><b style="margin-top:15px">MARKET</b><p>Lorem ipsum dolor sit amet, cons ectetuer adipiscing elit, sed diam nonummy.</p></div>
  <div class="tile" style="left:275px;top:110px;background:var(--amber);border-bottom-right-radius:6px"><div style="width:7px;height:7px;border:1px solid #fff;border-radius:50%"></div><b>MISSION</b><p>Lorem ipsum dolor sit amet, cons ectetuer adipiscing elit, sed diam nonummy.</p></div>
  <div class="foot"><span>© 2025 NOVA Advisory Group. All rights reserved.</span><span>5</span></div>
</section>

<!-- 8 Bar chart -->
<section class="slide" style="left:420px;top:481px">
  <div class="heading"><b>Heading</b> Goes Here</div>
  <div class="brand"><i></i>NOVA</div>
  <svg class="abs" style="left:0;top:0" width="190" height="204" font-family="Work Sans, sans-serif">
    <g stroke="#e1e4ea" stroke-width=".4"><path d="M36 154h140M36 138h140M36 122h140M36 106h140M36 90h140M36 74h140M36 58h140"/></g>
    <g font-size="2.8" fill="#777" text-anchor="end"><text x="33" y="155">0</text><text x="33" y="139">1</text><text x="33" y="123">2</text><text x="33" y="107">3</text><text x="33" y="91">4</text><text x="33" y="75">5</text><text x="33" y="59">6</text></g>
    <rect x="46" y="66" width="8" height="88" fill="#1f3870"/><rect x="55" y="80" width="8" height="74" fill="#3566d6"/><rect x="64" y="101" width="8" height="53" fill="#14a89a"/>
    <rect x="92" y="66" width="8" height="88" fill="#1f3870"/><rect x="101" y="50" width="8" height="104" fill="#3566d6"/><rect x="110" y="88" width="8" height="66" fill="#14a89a"/>
    <rect x="138" y="62" width="8" height="92" fill="#1f3870"/><rect x="147" y="100" width="8" height="54" fill="#3566d6"/><rect x="156" y="88" width="8" height="66" fill="#14a89a"/>
    <g font-size="3.6" fill="#555" text-anchor="middle"><text x="59" y="164">Category 1</text><text x="105" y="164">Category 1</text><text x="151" y="164">Category 1</text></g>
    <g font-size="2.6" fill="#777"><circle cx="81" cy="170" r=".9" fill="#1f3870"/><text x="83" y="171">Series 1</text><circle cx="100" cy="170" r=".9" fill="#3566d6"/><text x="102" y="171">Series 1</text><circle cx="119" cy="170" r=".9" fill="#14a89a"/><text x="121" y="171">Series 1</text></g>
  </svg>
  <div class="abs" style="left:194px;top:53px;width:21px;height:21px;border-radius:50%;background:var(--navy);color:#fff;font-size:8px;font-weight:700;text-align:center;line-height:21px">1</div>
  <div class="abs" style="left:194px;top:96px;width:21px;height:21px;border-radius:50%;background:var(--blue);color:#fff;font-size:8px;font-weight:700;text-align:center;line-height:21px">2</div>
  <div class="abs" style="left:194px;top:139px;width:21px;height:21px;border-radius:50%;background:var(--teal);color:#fff;font-size:8px;font-weight:700;text-align:center;line-height:21px">3</div>
  <div class="abs" style="left:222px;top:50px;width:112px"><div style="font-size:6px;font-weight:600;color:var(--navy)">Lorem ipsum dolor.</div><div class="tt" style="font-size:4.3px">Lorem ipsumectetuer adipiscing elit, sed diam nonummy nibh euismod tincidunt sed diam nonummy nibhunt</div></div>
  <div class="abs" style="left:222px;top:93px;width:112px"><div style="font-size:6px;font-weight:600;color:var(--blue)">Lorem ipsum dolor.</div><div class="tt" style="font-size:4.3px">Lorem ipsumectetuer adipiscing elit, sed diam nonummy nibh euismod tincidunt sed diam nonummy nibhunt</div></div>
  <div class="abs" style="left:222px;top:136px;width:112px"><div style="font-size:6px;font-weight:600;color:var(--teal)">Lorem ipsum dolor.</div><div class="tt" style="font-size:4.3px">Lorem ipsumectetuer adipiscing elit, sed diam nonummy nibh euismod tincidunt sed diam nonummy nibhunt</div></div>
  <div class="foot"><span>© 2025 NOVA Advisory Group. All rights reserved.</span><span>5</span></div>
</section>

<!-- 9 Three options -->
<section class="slide" style="left:798px;top:481px">
  <div class="heading"><b>Heading</b> Goes Here</div>
  <div class="brand"><i></i>NOVA</div>
  <svg class="abs" style="left:23px;top:92px" width="40" height="42"><polygon points="0,0 18,0 40,21 18,42 0,42 22,21" fill="#e9eaed"/></svg>
  <div class="photo" role="img" aria-label="Colleagues discussing at a laptop" style="left:85px;top:53px;width:66px;height:78px"></div>
  <div class="photo" role="img" aria-label="Meeting room with a presenter" style="left:172px;top:53px;width:66px;height:78px"></div>
  <div class="photo" role="img" aria-label="Business partners shaking hands" style="left:258px;top:53px;width:66px;height:78px"></div>
  <div class="abs" style="left:85px;top:135px;width:66px"><div style="font-size:6px;font-weight:600;color:var(--teal)">First <span style="color:var(--navy)">Option</span></div><div class="t" style="font-size:2.7px">Lorem ipsum dolor sit consectetuer adipiscing elit, sed diam nonummy nibh euismod tincidunt ut dolore magna aliquam erat volutpat. Ut wisi enim ad minim veniam, quis nostrud</div></div>
  <div class="abs" style="left:172px;top:135px;width:66px"><div style="font-size:6px;font-weight:600;color:var(--blue)">Second <span style="color:var(--navy)">Option</span></div><div class="t" style="font-size:2.7px">Lorem ipsum dolor sit consectetuer adipiscing elit, sed diam nonummy nibh euismod tincidunt ut dolore magna aliquam erat volutpat. Ut wisi enim ad minim veniam, quis nostrud</div></div>
  <div class="abs" style="left:258px;top:135px;width:66px"><div style="font-size:6px;font-weight:600;color:var(--amber)">Third <span style="color:var(--navy)">Option</span></div><div class="t" style="font-size:2.7px">Lorem ipsum dolor sit consectetuer adipiscing elit, sed diam nonummy nibh euismod tincidunt ut dolore magna aliquam erat volutpat. Ut wisi enim ad minim veniam, quis nostrud</div></div>
  <div class="foot"><span>© 2025 NOVA Advisory Group. All rights reserved.</span><span>6</span></div>
</section>

<!-- 10 Text + bullets -->
<section class="slide" style="left:39px;top:707px">
  <div class="heading"><b>Heading</b> Goes Here</div>
  <div class="brand"><i></i>NOVA</div>
  <div class="abs" style="left:26px;top:44px;width:150px">
    <div style="font-size:7px;font-weight:500;color:var(--navy)"><span class="num">01.</span> Text Added Here</div>
    <p class="t" style="font-size:3.2px;margin-top:2px;text-align:justify">Lorem ipsum dolor sit amet, cons ectetuer adipiscing elit, sed diam nonummy nibh euismod tincidunt ut laoreet dolore magna aliquam erat volutpat. Ut wisi enim ad minim veniam, quis nostrud exerci tation ullamcorper suscipit lobortis nisl ut aliquip ex ea commodo consequat.</p>
    <p class="t" style="font-size:3.2px;margin-top:4px;text-align:justify">Lorem ipsum dolor sit amet, consectetuer adipiscing elit, sed diam nonummy nibh euismod tincidunt ut laoreet dolore magna aliquam erat volutpat. Ut wisi enim ad minim veniam, quis nostrud exerci tation ullamcorper suscipit lobortis nisl ut aliquip ex ea commodo consequat.</p>
    <div style="font-size:7px;font-weight:500;color:var(--navy);margin-top:9px"><span class="num" style="color:var(--amber)">02.</span> Text Added Here</div>
    <p class="t" style="font-size:3.2px;margin-top:2px;text-align:justify">Lorem ipsum dolor sit amet, cons ectetuer adipiscing elit, sed diam nonummy nibh euismod tincidunt ut laoreet dolore magna aliquam erat volutpat. Ut wisi enim ad minim veniam, quis nostrud exerci tation ullamcorper suscipit lobortis nisl ut aliquip ex ea commodo consequat.</p>
    <p class="t" style="font-size:3.2px;margin-top:4px;text-align:justify">Lorem ipsum dolor sit amet, consectetuer adipiscing elit, sed diam nonummy nibh euismod tincidunt ut laoreet dolore magna aliquam erat volutpat. Ut wisi enim ad minim veniam, quis nostrud exerci tation ullamcorper suscipit lobortis nisl ut aliquip ex ea commodo consequat.</p>
  </div>
  <div class="abs" style="left:196px;top:56px;font-size:7.3px;color:var(--navy);line-height:20.4px">
    <div><span style="color:var(--teal)">•</span> Fits Your Business Or Products</div>
    <div><span style="color:var(--teal)">•</span> Is Easy To Spell And Remember</div>
    <div><span style="color:var(--teal)">•</span> Fits Your Business Or Products</div>
    <div><span style="color:var(--teal)">•</span> Is Easy To Spell And Remember</div>
    <div><span style="color:var(--teal)">•</span> Fits Your Business Or Products</div>
    <div><span style="color:var(--teal)">•</span> Is Easy To Spell And Remember</div>
  </div>
  <div class="foot"><span>© 2025 NOVA Advisory Group. All rights reserved.</span><span>7</span></div>
</section>

<!-- 11 Puzzle wheel -->
<section class="slide" style="left:420px;top:707px">
  <div class="heading"><b>Heading</b> Goes Here</div>
  <div class="brand"><i></i>NOVA</div>
  <svg class="abs" style="left:131px;top:59px" width="102" height="102" viewBox="-51 -51 102 102">
    <path d="M-1.5 -50 A50 50 0 0 0 -50 -1.5 L-26 -1.5 A26 26 0 0 1 -1.5 -26 Z" fill="#1f3870"/>
    <path d="M1.5 -50 A50 50 0 0 1 50 -1.5 L26 -1.5 A26 26 0 0 0 1.5 -26 Z" fill="#14a89a"/>
    <path d="M-1.5 50 A50 50 0 0 1 -50 1.5 L-26 1.5 A26 26 0 0 0 -1.5 26 Z" fill="#f29a3d"/>
    <path d="M1.5 50 A50 50 0 0 0 50 1.5 L26 1.5 A26 26 0 0 1 1.5 26 Z" fill="#3566d6"/>
    <g fill="#fff"><circle cx="0" cy="-38" r="4"/><circle cx="-38" cy="0" r="4"/><circle cx="38" cy="0" r="4"/><circle cx="0" cy="38" r="4"/></g>
    <g fill="none" stroke="#fff" stroke-width="1"><circle cx="-24" cy="-24" r="4.5"/><circle cx="-24" cy="-24" r="1.8"/><path d="M20 -20 l8 -8 M22 -26 l6 -2 l-2 6"/><rect x="-28" y="19" width="7" height="8"/><circle cx="24" cy="24" r="4.5"/><circle cx="24" cy="24" r="1.8"/></g>
  </svg>
  <div class="abs" style="left:157px;top:85px;width:52px;height:52px;border-radius:50%;background:#fff;display:flex;align-items:center;justify-content:center;text-align:center;font-size:8.5px;font-weight:700;color:var(--ink);line-height:1.05">Text<br>Added</div>
  <div class="abs" style="left:28px;top:60px;width:95px;text-align:right"><div style="font-size:6.3px;font-weight:600;color:var(--navy)">Text Here</div><div class="t" style="font-size:3.4px;color:#666">Lorem ipsum dolor sit amet, consectetuer adipiscing elit, sed diammy nibh euismod tincidunt ut laoreet dolore</div></div>
  <div class="abs" style="left:28px;top:133px;width:95px;text-align:right"><div style="font-size:6.3px;font-weight:600;color:var(--amber)">Text Here</div><div class="t" style="font-size:3.4px;color:#666">Lorem ipsum dolor sit amet, consectetuer adipiscing elit, sed diammy nibh euismod tincidunt ut laoreet dolore</div></div>
  <div class="abs" style="left:243px;top:60px;width:95px"><div style="font-size:6.3px;font-weight:600;color:var(--teal)">Text Here</div><div class="t" style="font-size:3.4px;color:#666">Lorem ipsum dolor sit amet, consectetuer adipiscing elit, sed diammy nibh euismod tincidunt ut laoreet dolore</div></div>
  <div class="abs" style="left:243px;top:133px;width:95px"><div style="font-size:6.3px;font-weight:600;color:var(--blue)">Text Here</div><div class="t" style="font-size:3.4px;color:#666">Lorem ipsum dolor sit amet, consectetuer adipiscing elit, sed diammy nibh euismod tincidunt ut laoreet dolore</div></div>
  <div class="foot"><span>© 2025 NOVA Advisory Group. All rights reserved.</span><span>8</span></div>
</section>

<!-- 12 Timeline -->
<section class="slide" style="left:798px;top:707px">
  <div class="heading"><b>Heading</b> Goes Here</div>
  <div class="brand"><i></i>NOVA</div>
  <svg class="abs" style="left:0;top:0" width="363" height="204" font-family="Work Sans, sans-serif">
    <polygon points="40,106 92,106 98,117 34,117" fill="#14a89a"/>
    <polygon points="92,106 157,106 151,117 98,117" fill="#1f3870"/>
    <polygon points="157,106 210,106 216,117 151,117" fill="#3566d6"/>
    <polygon points="210,106 275,106 269,117 216,117" fill="#1f3870"/>
    <polygon points="275,106 322,106 328,117 269,117" fill="#f29a3d"/>
    <g font-size="5" fill="#fff" text-anchor="middle"><text x="64" y="113.5">1990</text><text x="124" y="113.5">2001</text><text x="183" y="113.5">2007</text><text x="242" y="113.5">2012</text><text x="301" y="113.5">2020</text></g>
    <g stroke-width=".9"><path d="M64 88v14" stroke="#14a89a"/><path d="M183 88v14" stroke="#3566d6"/><path d="M301 88v14" stroke="#f29a3d"/></g>
    <circle cx="64" cy="88" r="1.8" fill="#14a89a"/><circle cx="183" cy="88" r="1.8" fill="#3566d6"/><circle cx="301" cy="88" r="1.8" fill="#f29a3d"/>
    <g stroke="#1f3870" stroke-width=".9"><path d="M124 121v14M242 121v14"/></g>
    <g fill="#1f3870"><circle cx="124" cy="135" r="1.8"/><circle cx="242" cy="135" r="1.8"/></g>
    <g text-anchor="middle" font-size="5" font-weight="600" fill="#1f3870"><text x="64" y="63">YOUR TITLE</text><text x="183" y="63">YOUR TITLE</text><text x="301" y="63">YOUR TITLE</text></g>
    <g text-anchor="middle" font-size="5" font-weight="600" fill="#14a89a"><text x="124" y="151">YOUR TITLE</text><text x="242" y="151">YOUR TITLE</text></g>
    <g text-anchor="middle" font-size="3.6" fill="#8b93a3"><text x="64" y="69">Refers to a good or</text><text x="64" y="73.5">service being offered</text><text x="183" y="69">Refers to a good or</text><text x="183" y="73.5">service being offered</text><text x="301" y="69">Refers to a good or</text><text x="301" y="73.5">service being offered</text><text x="124" y="157">Refers to a good or</text><text x="124" y="161.5">service being offered</text><text x="242" y="157">Refers to a good or</text><text x="242" y="161.5">service being offered</text></g>
  </svg>
  <div class="foot"><span>© 2025 NOVA Advisory Group. All rights reserved.</span><span>8</span></div>
</section>

<!-- 13 Phones -->
<section class="slide" style="left:39px;top:929px">
  <svg class="abs" style="left:0;top:0" width="363" height="204"><polygon points="140,190 245,0 350,190" fill="#eef1f2"/></svg>
  <div class="heading"><b>Heading</b> Goes Here</div>
  <div class="brand"><i></i>NOVA</div>
  <div class="abs t" style="left:17px;top:41px;width:130px;font-size:4px;color:#666">Lorem ipsum dolor sit amet, consectetuer adipiscing elit, sed diam nonummy nibh euismod tincidunt ut laoreet dolore magna aliquam erat volutpat. Ut wisi enim ad minim veniam,<br><br>quis nostrud exerci tation ullamcorper suscipit lobortis nisl ut aliquip ex ea commodo consequat. Duis autem vel eum iriure dolor in hendrerit in vulputate velit esse</div>
  <div class="abs" style="left:32px;top:102px;width:110px;display:flex;gap:5px"><span class="step" style="background:var(--teal)">1.</span><div><div style="font-size:4.6px;font-weight:600;color:var(--navy)">Lorem Ipsum</div><div class="t" style="font-size:2.7px">Lorem ipsum dolor sit amet, consectetuer adipiscing elit, sed diam nonummy nibh euismod tincid</div></div></div>
  <div class="abs" style="left:32px;top:127px;width:110px;display:flex;gap:5px"><span class="step" style="background:var(--blue)">2.</span><div><div style="font-size:4.6px;font-weight:600;color:var(--navy)">Lorem Ipsum</div><div class="t" style="font-size:2.7px">Lorem ipsum dolor sit amet, consectetuer adipiscing elit, sed diam nonummy nibh euismod tincid</div></div></div>
  <div class="abs" style="left:32px;top:152px;width:110px;display:flex;gap:5px"><span class="step" style="background:var(--amber)">3.</span><div><div style="font-size:4.6px;font-weight:600;color:var(--navy)">Lorem Ipsum</div><div class="t" style="font-size:2.7px">Lorem ipsum dolor sit amet, consectetuer adipiscing elit, sed diam nonummy nibh euismod tincid</div></div></div>
  <div class="phone" style="left:174px;top:35px;padding:9px 4px"><i></i><div style="font-size:4.4px;color:var(--navy);line-height:1.15">Lorem ipsum dolor</div><svg width="12" height="9" style="margin:10px 0 0 11px" fill="none" stroke="#14a89a" stroke-width=".7"><path d="M1 1h4l1 1 1-1h4v7h-4l-1 1-1-1h-4z M6 2v6"/></svg><div class="t" style="font-size:2.3px;margin-top:3px">To introduce the students to the changing landscape of marketing and equip them with knowledge and tools to navigate the digital marketing world</div></div>
  <div class="phone" style="left:229px;top:63px;padding:18px 4px 4px"><i></i><div style="font-size:4.4px;color:var(--navy);line-height:1.15">Dolor sit amet, conse</div><svg width="12" height="12" style="margin:4px 0 0 11px" fill="none" stroke="#3566d6" stroke-width=".7"><path d="M2 2h3v3h3v3h3M2 6h3v4"/></svg><div class="t" style="font-size:2.3px;margin-top:3px">You will learn concepts and ideas in digital marketing as well as how to use different tools and strategies to optimize your digital marketing campaigns.</div></div>
  <div class="phone" style="left:282px;top:92px;padding:18px 4px 4px"><i></i><div style="font-size:4.4px;color:var(--navy)">Consec</div><div style="font-size:4px;color:var(--grey);letter-spacing:1px">• • • •</div><svg width="12" height="12" style="margin:3px 0 0 11px" fill="none" stroke="#f29a3d" stroke-width=".7"><circle cx="6" cy="6" r="5"/><path d="M3.5 8.5 L6 3 L8.5 8.5 M4.5 6.8h3"/></svg><div class="t" style="font-size:2.3px;margin-top:3px">You are required to pass 90% of the evaluation test to obtain the certificate. The evaluation test can only be taken 3 times.</div></div>
  <div class="foot"><span>© 2025 NOVA Advisory Group. All rights reserved.</span><span>8</span></div>
</section>

<!-- 14 Two columns -->
<section class="slide" style="left:420px;top:929px">
  <div class="heading"><b>Heading</b> Goes Here</div>
  <div class="brand"><i></i>NOVA</div>
  <div class="abs" style="left:33px;top:47px;width:141px">
    <div style="font-size:10px;font-weight:500;color:var(--navy)"><span style="color:var(--teal);font-weight:600">01.</span> Text Added Here</div>
    <p class="t" style="font-size:3.3px;margin-top:3px;text-align:justify;color:#666">Lorem ipsum dolor sit amet, cons ectetuer adipiscing elit, sed diam nonummy nibh euismod tincidunt ut laoreet dolore magna aliquam erat volutpat. Ut wisi enim ad minim veniam, quis nostrud exerci tation ullamcorper suscipit lobortis nisl ut aliquip ex ea commodo consequat. Lorem ipsum dolor sit amet, consectetuer adipiscing elit, sed diam nonummy nibh euismod tincidunt ut laoreet dolore magna aliquam erat volutpat. Utstrud exerci tation ullamcorper suscipit lobortis nisl ut aliquip ex ea commodo consequat.</p>
    <p class="t" style="font-size:3.3px;margin-top:5px;text-align:justify;color:#666">Lorem ipsum dolor sit amet, cons ectetuer adipiscing elit, sed diam nonummy nibh euismod tincidunt ut laoreet dolore magna aliquam erat volutpat. Ut wisi enim ad minim veniam, quis nostrud exerci tation ullamcorper suscipit lobortis nisl ut aliquip ex ea commodo consequat.</p>
    <p class="t" style="font-size:3.3px;margin-top:5px;text-align:justify;color:#666">Lorem ipsum dolor sit amet, consectetuer adipiscing elit, sed diam nonummy nibh euismod tincidunt ut laoreet dolore magna aliquam erat volutpat. Ut wisi enim ad minim veniam, cons ectetuer adipiscing elit, quis nostrud exerci tation ullamcorper suscipit lobortis nisl ut aliquip.</p>
  </div>
  <div class="abs" style="left:190px;top:47px;width:141px">
    <div style="font-size:10px;font-weight:500;color:var(--navy)"><span style="color:var(--amber);font-weight:600">02.</span> Text Added Here</div>
    <p class="t" style="font-size:3.3px;margin-top:3px;text-align:justify;color:#666">Lorem ipsum dolor sit amet, cons ectetuer adipiscing elit, sed diam nonummy nibh euismod tincidunt ut laoreet dolore magna aliquam erat volutpat. Ut wisi enim ad minim veniam, quis nostrud exerci tation ullamcorper suscipit lobortis nisl ut aliquip ex ea commodo consequat. Lorem ipsum dolor sit amet, consectetuer adipiscing elit, sed diam nonummy nibh euismod tincidunt ut laoreet dolore magna aliquam erat volutpat. Utstrud exerci tation ullamcorper suscipit lobortis nisl ut aliquip ex ea commodo consequat.</p>
    <p class="t" style="font-size:3.3px;margin-top:5px;text-align:justify;color:#666">Lorem ipsum dolor sit amet, cons ectetuer adipiscing elit, sed diam nonummy nibh euismod tincidunt ut laoreet dolore magna aliquam erat volutpat. Ut wisi enim ad minim veniam, quis nostrud exerci tation ullamcorper suscipit lobortis nisl ut aliquip ex ea commodo consequat.</p>
    <p class="t" style="font-size:3.3px;margin-top:5px;text-align:justify;color:#666">Lorem ipsum dolor sit amet, consectetuer adipiscing elit, sed diam nonummy nibh euismod tincidunt ut laoreet dolore magna aliquam erat volutpat. Ut wisi enim ad minim veniam, cons ectetuer adipiscing elit, quis nostrud exerci tation ullamcorper suscipit lobortis nisl ut aliquip.</p>
  </div>
  <div class="foot"><span>© 2025 NOVA Advisory Group. All rights reserved.</span><span>8</span></div>
</section>

<!-- 15 Thank you -->
<section class="slide" style="left:798px;top:929px">
  <div class="abs" role="img" aria-label="Blue-tinted photo of a business handshake" style="left:0;top:25px;width:363px;height:154px;background:linear-gradient(100deg,#6f97e0,#86aae9 50%,#7fcfc4)"></div>
  <i class="abs" style="left:0;top:176px;width:363px;height:3px;background:var(--amber)"></i>
  <div class="abs" style="left:50px;top:86px;display:flex;align-items:center;gap:5px;font-size:21px;font-weight:700;color:var(--navy)"><i style="display:block;width:12px;height:12px;background:var(--teal)"></i>NOVA</div>
  <div class="abs" style="left:200px;top:50px;font-size:22px;font-weight:700;color:var(--navy)">Thank You</div>
  <svg class="abs" style="left:200px;top:86px" width="11" height="70" fill="#1f3870">
    <path d="M2 1 h3 l1 3 -2 1.5 a7 7 0 0 0 3 3 l1.5 -2 3 1 v3 a9 9 0 0 1 -9.5 -9.5z"/>
    <path d="M1 28 l10 -4 -4 10 -1.5 -4.5z"/>
    <path d="M5.5 48 l5.5 5 h-1.5 v5 h-3 v-3 h-2 v3 h-3 v-5 h-1.5z"/>
  </svg>
  <div class="abs" style="left:222px;top:85px;font-size:5px;color:var(--ink);line-height:1.25">+65 6100 2040<br>+65 6100 2041</div>
  <div class="abs" style="left:222px;top:108px;font-size:5px;color:var(--ink);line-height:1.25">www.novaadvisory.example<br>hello@novaadvisory.example</div>
  <div class="abs" style="left:222px;top:129px;font-size:5px;color:var(--ink);line-height:1.3">8 Marina Lane, Singapore,<br>Singapore 018980.</div>
</section>

</body>
</html>
```